Business card - fitness trainer

Hello all, we have the need for a business card and would like to work with you to utilize your skills.

We would like the background to be black and use elements of the logo and lettering in blue, yellow and white, if that is possible.

Please see the attached logo which we would like to incorporate.

http://www.artvendly.com/download-source-file.aspx?designid=5830416&type=source

I am having a hard time attaching the logo files so please let me know if you cannot see it

Thank you

Fitness

```html
<!DOCTYPE html>
<html lang="en">
<head>
<meta charset="utf-8">
<title>Vela Health and Fitness – Business Card</title>
<link href="https://fonts.googleapis.com/css2?family=Questrial&display=swap" rel="stylesheet">
<style>
  :root{
    --stage:#141414;
    --card-dark:#232323;
    --card-light:#f7f8f9;
    --brand-blue:#2f87c4;
    --brand-yellow:#f6b52e;
    --brand-yellow-clear:rgba(246,181,46,0);
    --ink-light:#ffffff;
  }
  *{margin:0;padding:0;box-sizing:border-box}
  html,body{width:1200px;height:871px;overflow:hidden;background:var(--stage)}
  body{font-family:"Questrial",sans-serif;display:flex;align-items:center;justify-content:center;gap:40px}
  .card{position:relative;width:560px;height:320px;overflow:hidden;border-radius:4px;box-shadow:0 10px 30px rgba(0,0,0,.6)}
  .card--front{background:var(--card-light);display:flex;align-items:center;justify-content:center}
  .brand{display:flex;align-items:center;gap:14px;color:var(--brand-blue);font-size:72px;line-height:1;letter-spacing:1px}
  .brand__dot{width:26px;height:26px;border-radius:50%;background:var(--brand-yellow)}
  .card--back{background:var(--card-dark)}
  .card__accent{position:absolute;inset:0;background:radial-gradient(ellipse 75% 90% at 0% 100%,var(--brand-yellow) 0%,var(--brand-yellow-clear) 70%);opacity:.55}
  .details{position:absolute;top:32px;right:22px;text-align:right;color:var(--ink-light)}
  .details__name{color:var(--brand-yellow);font-size:24px;font-weight:400;letter-spacing:3px;text-transform:uppercase;line-height:1.2}
  .details__role{font-size:16px;letter-spacing:2px;text-transform:uppercase;margin-bottom:18px}
  .contact{list-style:none;font-size:15px;letter-spacing:1.2px}
  .contact__item{display:flex;align-items:center;justify-content:flex-end;gap:12px;height:30px;white-space:nowrap}
  .contact__icon{width:20px;height:20px;flex:none}
  .contact__icon--square{background:var(--brand-yellow);border-radius:2px}
</style>
</head>
<body>
  <section class="card card--front" aria-label="Card front">
    <div class="brand"><span class="brand__dot"></span><span class="brand__name">vela</span></div>
  </section>

  <section class="card card--back" aria-label="Card back">
    <div class="card__accent" role="img" aria-label="Yellow decorative accent sweeping across the lower left of the card"></div>
    <div class="details">
      <h1 class="details__name">Dana Whitcombe</h1>
      <p class="details__role">Fitness Trainer</p>
      <ul class="contact">
        <li class="contact__item">/vela-healthandfitness<span class="contact__icon contact__icon--square"></span></li>
        <li class="contact__item">@vela-healthandfitness<span class="contact__icon contact__icon--square"></span></li>
        <li class="contact__item">Sample address 766, Sample Town 01234
          <svg class="contact__icon" viewBox="0 0 20 20" aria-label="Address"><path d="M10 1a6 6 0 0 0-6 6c0 5 6 12 6 12s6-7 6-12a6 6 0 0 0-6-6z" fill="none" stroke="var(--brand-yellow)" stroke-width="2"/><circle cx="10" cy="7" r="2" fill="var(--brand-yellow)"/></svg></li>
        <li class="contact__item">(0) 32 555 01 23
          <svg class="contact__icon" viewBox="0 0 20 20" aria-label="Phone"><rect x="4" y="1" width="12" height="18" rx="2" fill="none" stroke="var(--brand-yellow)" stroke-width="2"/><rect x="7" y="15" width="6" height="1.5" fill="var(--brand-yellow)"/></svg></li>
        <li class="contact__item">danawhitcombe@mailbox.com
          <svg class="contact__icon" viewBox="0 0 20 20" aria-label="Email"><rect x="1" y="4" width="18" height="12" fill="none" stroke="var(--brand-yellow)" stroke-width="2"/><path d="M1 4l9 7 9-7" fill="none" stroke="var(--brand-yellow)" stroke-width="2"/></svg></li>
      </ul>
    </div>
  </section>
</body>
</html>
```